K & R Acreage Works. Business card design

We need a business card designed for a new business. We have a bulldozer and tractor service. We clear land and make wildlife food plots. We provide disking, bush hogging, and site prep services.
I have attached an image of a business card that I like and would like my business cards to look similar.

Target Market(s)

anyone needing bulldozer and/or tractor services

Industry/Entity Type

Business

Contact Information for Business Card

K & R Acreage Works, Operated by 7-M-Ranch
Doug Pelham
601-473-5826
dpr4178@mailvexo.com

Font styles to use
Sans Serif

Colors

Designer to choose colors to be used in the design.

Requirements
Must have
• image of tractor and bulldozer
• Land Clearing
• Wildlife food plots
• Bush Hogging
• Disking
• Site prep
Nice to have
• i have included a image of a business card that i like. I would like mine to be similar.

```html
<!DOCTYPE html>
<html lang="en">
<head>
<meta charset="utf-8">
<title>K &amp; R Acreage Works – Business Card</title>
<link rel="stylesheet" href="https://fonts.googleapis.com/css2?family=Bebas+Neue&family=Open+Sans:wght@400;700&family=Arimo:wght@400;700&display=swap">
<style>
  :root {
    --page-bg: #ece9e4;
    --card-bg: #333333;
    --accent: #e8780f;
    --text-light: #ffffff;
    --text-muted: #b9b9b9;
    --services-text: #e6e6e6;
    --sky: #8fb6e0;
    --foliage: #5f8a3a;
    --ground: #7a6a4a;
  }
  * { margin: 0; padding: 0; box-sizing: border-box; }
  html, body {
    width: 1200px; height: 900px; overflow: hidden;
    background: var(--page-bg);
  }
  .canvas { position: relative; width: 1200px; height: 900px; }
  .card {
    position: absolute; left: 406px; top: 133px;
    width: 445px; height: 720px;
    background: var(--card-bg);
    box-shadow: 0 4px 10px rgba(0,0,0,.25);
    text-align: center;
  }
  .contact { position: absolute; top: 42px; left: 0; right: 0; }
  .contact-name {
    font-family: "Arimo", Arial, sans-serif; font-weight: 700;
    font-size: 30px; color: var(--accent); line-height: 36px;
  }
  .contact-line {
    font-family: "Arimo", Arial, sans-serif; font-size: 20px;
    color: var(--text-light); line-height: 26px;
  }
  .brand-mark {
    position: absolute; left: 167px; top: 170px;
    width: 110px; height: 110px;
    border: 4px solid var(--accent); border-radius: 50%;
  }
  .brand-name {
    position: absolute; top: 288px; left: 0; right: 0;
    font-family: "Bebas Neue", "Arial Narrow", sans-serif;
    font-size: 38px; color: var(--accent); line-height: 40px;
    letter-spacing: .5px;
  }
  .brand-operator {
    position: absolute; top: 324px; left: 0; right: 0;
    font-family: "Open Sans", Arial, sans-serif; font-weight: 700;
    font-size: 18px; color: var(--text-muted); line-height: 22px;
  }
  .photo { position: absolute; top: 362px; height: 245px; }
  .photo-dozer {
    left: 0; width: 265px;
    background: linear-gradient(to bottom, var(--sky) 0%, var(--foliage) 18%, #6f8f3d 60%, var(--ground) 100%);
  }
  .photo-tractor {
    left: 266px; width: 179px;
    background: linear-gradient(to bottom, var(--sky) 0%, #7aa0c9 22%, var(--foliage) 40%, #7b8d45 100%);
  }
  .services {
    position: absolute; top: 630px; left: 0; right: 0;
    font-family: "Open Sans", Arial, sans-serif; font-size: 21px;
    color: var(--services-text); line-height: 30px;
  }
</style>
</head>
<body>
<div class="canvas">
  <section class="card">
    <div class="contact">
      <p class="contact-name">Doug Pelham</p>
      <p class="contact-line">Tel: 601-473-5826</p>
      <p class="contact-line">Email: dpr4178@mailvexo.com</p>
    </div>
    <div class="brand-mark"></div>
    <p class="brand-name">K &amp; R Acreage Works</p>
    <p class="brand-operator">OPERATED BY 7-M-RANCH</p>
    <div class="photo photo-dozer" role="img" aria-label="Photo of a yellow bulldozer clearing land at a wooded site"></div>
    <div class="photo photo-tractor" role="img" aria-label="Photo of an orange tractor with front loader in a grassy field"></div>
    <div class="services">
      <p>Land Clearing | Wildlife Food Plots</p>
      <p>Bush Hogging | Disking | Site Prep</p>
    </div>
  </section>
</div>
</body>
</html>
```